ReadNest Learning App for Children with Dyslexia

Project Description:

We are seeking a talented UI/UX designer to create engaging and intuitive designs for Readnest, an innovative educational app designed to help children learn letters and words through a multisensory learning approach. The app aims to be particularly helpful for children with dyslexia, providing a supportive and interactive learning environment.

Key App Features & Design Requirements:

Account Creation Screen: Design a welcoming and straightforward sign-up page that allows users to register with their email or continue with Quorvix. The design should be clean, focusing on user-friendliness and accessibility, adhering to our terms of service and privacy policy.

Main Screen Design: The main screen should allocate at least 4/6 of its height to the interactive drawing area. It needs to display word prompts in both correct and scrambled orders and include options to "Show all Words," "Play all words," and a search function. The interface should be vibrant, engaging, and easy to navigate for children.

Profile Section: Create a user-friendly profile page that allows users to edit their profile image, name, username, email, links, and bio. The design should be clean and encourage user engagement.

NestStats Page: This section will display the user's learning progress, including rankings, a learning curve, and recently learned words. It should visually represent progress in a motivating and understandable way, suitable for a younger audience.

Visual and Auditory Feedback Implementation: Incorporate elements that support visual and auditory feedback, using dyslexia-friendly formats. This includes choosing appropriate colors, fonts, and auditory cues.

Accessibility and Customization Settings: Designs should include settings for adjusting visual contrast, font size, and the word list to accommodate individual preferences and needs.

Feel free to add more interactions and/or pages.

Design preferences:

Color Scheme: Use a bright, inviting color palette that stimulates learning and engagement without overwhelming the users.
Font Selection: Opt for fonts that are readable and accessible, particularly for users with dyslexia.
Icons and Graphics: Design custom icons and graphics that are cohesive with the app's theme and purpose. Illustrations should be simple, relatable, and supportive of the learning process.

Target Market(s)

Educational

Industry/Entity Type

Educational

Colors
0054AA
0677BA
7BADD7
CADEEF
E8F1F8
0094D4
00A9DD
6FCCEA
C7EBF8
E9F6FB

Requirements
Must have
• Educational app, a writing area, scoring and account management
Nice to have
• Statistics, Ranking Page, Settings and some nice visual features

```html
<!DOCTYPE html>
<html lang="en">
<head>
<meta charset="utf-8">
<title>Readnest – Writing, Word Play and NestStats screens</title>
<link href="https://fonts.googleapis.com/css2?family=Poppins:wght@400;500;600;700&display=swap" rel="stylesheet">
<style>
:root{
  --blue:#0054AA;
  --blue-mid:#0677BA;
  --sky:#00A9DD;
  --sky-soft:#6FCCEA;
  --sky-pale:#C7EBF8;
  --tile:#E9F6FB;
  --ink:#2E3440;
  --ink-soft:#4A5260;
  --muted:#9AA0A8;
  --line:#E4E6EA;
  --canvas:#F4F4F4;
  --screen-bg:#F7F7F7;
  --white:#FFFFFF;
  --black:#000000;
}
*{box-sizing:border-box;margin:0;padding:0}
html,body{width:1200px;height:1020px;overflow:hidden;background:var(--white);font-family:'Poppins',sans-serif;color:var(--ink)}
.stage{position:relative;width:1200px;height:1020px}
.phone{position:absolute;width:327px;border:3px solid var(--black);border-radius:30px;overflow:hidden;background:var(--screen-bg)}
.phone > *{position:absolute}
.status-bar{left:0;top:0;width:100%;height:37px;background:var(--black);color:var(--white);font-size:11px;font-weight:600}
.status-bar .time{position:absolute;left:19px;top:12px}
.status-bar svg{position:absolute;top:13px}
.app-header{left:0;top:37px;width:100%;height:42px;background:var(--white);border-bottom:1px solid #EFEFEF}
.app-header .title{position:absolute;left:36px;top:12px;font-size:12px;font-weight:500}
.app-header .title.center{left:0;width:100%;text-align:center;font-size:15px;top:10px}
.app-header svg{position:absolute}
.toolbar{left:0;top:79px;width:100%;height:42px;background:var(--white)}
.toolbar svg,.toolbar .color-dot{position:absolute;top:12px}
.color-dot{width:17px;height:17px;border-radius:50%;background:var(--blue)}
.drawing-area{left:0;top:121px;width:100%;height:342px;background:var(--canvas)}
.tabs{left:11px;top:463px;width:299px;height:43px;border-bottom:2px solid var(--line)}
.tab{position:absolute;top:0;width:150px;height:43px;display:flex;align-items:center;justify-content:center;gap:6px;font-size:11.5px;font-weight:500;color:var(--muted)}
.tab.active{color:var(--blue);font-weight:600;border-bottom:2px solid var(--blue);height:45px}
.tab:first-child{left:0}.tab:last-child{left:150px}
.sentence-card{left:11px;width:299px;height:95px;border-radius:24px;background:var(--tile);padding:20px 30px;font-size:18px;font-weight:600;line-height:27px;color:var(--ink)}
.word-tile{background:var(--tile);border-radius:28px;display:flex;align-items:center;justify-content:center;font-weight:600;color:var(--ink)}
.primary-button{left:11px;top:836px;width:299px;height:47px;border-radius:24px;background:var(--blue);color:var(--white);font-size:12px;font-weight:600;display:flex;align-items:center;justify-content:center}
.avatar{left:12px;top:47px;width:22px;height:22px;border-radius:50%;background:radial-gradient(circle at 50% 40%,#C9A48A,#5E6B7A)}
.pill{top:91px;height:39px;border-radius:20px;background:#EEEEEE;font-size:12px;font-weight:500;color:var(--ink-soft);display:flex;align-items:center;justify-content:center}
.pill.active{background:var(--blue);color:var(--white);font-size:13px}
.rank-card{top:142px;height:86px;border-radius:43px;background:var(--tile)}
.badge{position:absolute;width:46px;height:46px;border-radius:50%;background:var(--sky-pale);display:flex;align-items:center;justify-content:center}
.rank-card .label{position:absolute;left:84px;top:22px;font-size:10px;color:var(--ink-soft)}
.rank-card .value{position:absolute;left:84px;top:34px;font-size:31px;font-weight:600;color:var(--ink);line-height:38px}
.rank-card .value small{font-size:15px;font-weight:600;margin:0 4px 0 1px}
.stat-card{left:12px;width:297px;background:var(--white);border-radius:24px;border:1px solid #F0F0F0}
.stat-card .month{position:absolute;left:15px;font-size:10px;color:var(--ink-soft)}
.stat-card .heading{position:absolute;left:15px;font-size:15px;font-weight:500;color:var(--ink)}
.chart{position:absolute;left:0;top:0}
.chart text{font-family:'Poppins',sans-serif;font-size:10px;fill:var(--ink-soft)}
.word-row{position:absolute;left:15px;width:250px;border-top:1px solid var(--line);padding-top:7px;font-size:11px;font-weight:500;color:var(--ink-soft)}
</style>
</head>
<body>
<main class="stage">

  <!-- Writing screen: sentence list -->
  <section class="phone" style="left:70px;top:51px;height:749px">
    <div class="status-bar"><span class="time">9:41</span>
      <svg style="left:261px" width="16" height="12" viewBox="0 0 16 12"><path d="M1 4a10 10 0 0 1 14 0M3.5 6.5a6.5 6.5 0 0 1 9 0M6 9a3 3 0 0 1 4 0" fill="none" stroke="#fff" stroke-width="1.4" stroke-linecap="round"/></svg>
      <svg style="left:285px" width="17" height="11" viewBox="0 0 17 11"><rect x="1" y="1" width="13" height="9" rx="2.5" fill="none" stroke="#fff" stroke-width="1.2"/><rect x="3.5" y="3.5" width="2" height="4" fill="#fff"/><rect x="6.5" y="3.5" width="2" height="4" fill="#fff"/><rect x="15" y="4" width="1.5" height="3" fill="#fff"/></svg>
    </div>
    <header class="app-header">
      <svg style="left:13px;top:14px" width="16" height="14" viewBox="0 0 16 14"><path d="M15 7H2M7 1.5 1.5 7 7 12.5" fill="none" stroke="#2E3440" stroke-width="1.4" stroke-linecap="round"/></svg>
      <span class="title">Word 1</span>
      <svg style="left:262px;top:12px" width="18" height="18" viewBox="0 0 18 18"><circle cx="8" cy="8" r="6.5" fill="none" stroke="#9AA0A8" stroke-width="1.3"/><path d="M13 13l4 4" stroke="#9AA0A8" stroke-width="1.3"/></svg>
      <svg style="left:293px;top:14px" width="16" height="13" viewBox="0 0 16 13"><path d="M1 1h14M1 6.5h10M1 12h7" stroke="#2E3440" stroke-width="1.4" stroke-linecap="round"/></svg>
    </header>
    <div class="toolbar">
      <svg style="left:16px" width="17" height="17" viewBox="0 0 17 17"><path d="M2 15l1-4 9-9 3 3-9 9zM10 4l3 3" fill="none" stroke="#2E3440" stroke-width="1.3" stroke-linejoin="round"/></svg>
      <svg style="left:53px" width="18" height="18" viewBox="0 0 18 18"><circle cx="9" cy="9" r="8" fill="none" stroke="#9AA0A8" stroke-width="1.2"/><path d="M5.5 5.5h7M9 5.5v8" stroke="#9AA0A8" stroke-width="1.2"/></svg>
      <svg style="left:92px" width="20" height="16" viewBox="0 0 20 16"><text x="0" y="13" font-family="Poppins,sans-serif" font-size="14" fill="#9AA0A8">Aa</text></svg>
      <svg style="left:132px" width="18" height="18" viewBox="0 0 18 18"><path d="M3 11l7-7 4 4-7 7H5zM2 17h14" fill="none" stroke="#9AA0A8" stroke-width="1.2" stroke-linejoin="round"/></svg>
      <span class="color-dot" style="left:170px"></span>
      <svg style="left:253px" width="18" height="17" viewBox="0 0 18 17"><path d="M6 1L1.5 5.5 6 10M2 5.5h8a6 6 0 0 1 6 6V16" fill="none" stroke="#2E3440" stroke-width="1.3" stroke-linecap="round"/></svg>
      <svg style="left:291px" width="18" height="17" viewBox="0 0 18 17"><path d="M12 1l4.5 4.5L12 10M16 5.5H8a6 6 0 0 0-6 6V16" fill="none" stroke="#9AA0A8" stroke-width="1.3" stroke-linecap="round"/></svg>
    </div>
    <div class="drawing-area" role="img" aria-label="Drawing canvas with the word Hello handwritten in blue"></div>
    <nav class="tabs">
      <div class="tab active"><svg width="16" height="16" viewBox="0 0 16 16"><g fill="none" stroke="#0054AA" stroke-width="1.4"><rect x="1" y="1" width="5.5" height="5.5" rx="1.5"/><rect x="9.5" y="1" width="5.5" height="5.5" rx="1.5"/><rect x="1" y="9.5" width="5.5" height="5.5" rx="1.5"/><rect x="9.5" y="9.5" width="5.5" height="5.5" rx="1.5"/></g></svg>Show all word</div>
      <div class="tab"><svg width="16" height="16" viewBox="0 0 16 16"><g fill="none" stroke="#9AA0A8" stroke-width="1.2"><rect x="1" y="1" width="5.5" height="5.5" rx="1.5"/><rect x="9.5" y="1" width="5.5" height="8" rx="1.5"/><rect x="1" y="9.5" width="5.5" height="5.5" rx="1.5"/><rect x="9.5" y="11.5" width="5.5" height="3.5" rx="1.5"/></g></svg>Play all words</div>
    </nav>
    <p class="sentence-card" style="top:518px">Hello, hope you are doing fine.</p>
    <p class="sentence-card" style="top:620px">Lorem ipsum dolor sit amet, consectetur</p>
  </section>

  <!-- Writing screen: scrambled word play -->
  <section class="phone" style="left:436px;top:51px;height:916px">
    <div class="status-bar"><span class="time">9:41</span>
      <svg style="left:261px" width="16" height="12" viewBox="0 0 16 12"><path d="M1 4a10 10 0 0 1 14 0M3.5 6.5a6.5 6.5 0 0 1 9 0M6 9a3 3 0 0 1 4 0" fill="none" stroke="#fff" stroke-width="1.4" stroke-linecap="round"/></svg>
      <svg style="left:285px" width="17" height="11" viewBox="0 0 17 11"><rect x="1" y="1" width="13" height="9" rx="2.5" fill="none" stroke="#fff" stroke-width="1.2"/><rect x="3.5" y="3.5" width="2" height="4" fill="#fff"/><rect x="6.5" y="3.5" width="2" height="4" fill="#fff"/><rect x="15" y="4" width="1.5" height="3" fill="#fff"/></svg>
    </div>
    <header class="app-header">
      <svg style="left:13px;top:14px" width="16" height="14" viewBox="0 0 16 14"><path d="M15 7H2M7 1.5 1.5 7 7 12.5" fill="none" stroke="#2E3440" stroke-width="1.4" stroke-linecap="round"/></svg>
      <span class="title">Word 1</span>
      <svg style="left:262px;top:12px" width="18" height="18" viewBox="0 0 18 18"><circle cx="8" cy="8" r="6.5" fill="none" stroke="#9AA0A8" stroke-width="1.3"/><path d="M13 13l4 4" stroke="#9AA0A8" stroke-width="1.3"/></svg>
      <svg style="left:293px;top:14px" width="16" height="13" viewBox="0 0 16 13"><path d="M1 1h14M1 6.5h10M1 12h7" stroke="#2E3440" stroke-width="1.4" stroke-linecap="round"/></svg>
    </header>
    <div class="toolbar">
      <svg style="left:16px" width="17" height="17" viewBox="0 0 17 17"><path d="M2 15l1-4 9-9 3 3-9 9zM10 4l3 3" fill="none" stroke="#2E3440" stroke-width="1.3" stroke-linejoin="round"/></svg>
      <svg style="left:53px" width="18" height="18" viewBox="0 0 18 18"><circle cx="9" cy="9" r="8" fill="none" stroke="#9AA0A8" stroke-width="1.2"/><path d="M5.5 5.5h7M9 5.5v8" stroke="#9AA0A8" stroke-width="1.2"/></svg>
      <svg style="left:92px" width="20" height="16" viewBox="0 0 20 16"><text x="0" y="13" font-family="Poppins,sans-serif" font-size="14" fill="#9AA0A8">Aa</text></svg>
      <svg style="left:132px" width="18" height="18" viewBox="0 0 18 18"><path d="M3 11l7-7 4 4-7 7H5zM2 17h14" fill="none" stroke="#9AA0A8" stroke-width="1.2" stroke-linejoin="round"/></svg>
      <span class="color-dot" style="left:170px"></span>
      <svg style="left:253px" width="18" height="17" viewBox="0 0 18 17"><path d="M6 1L1.5 5.5 6 10M2 5.5h8a6 6 0 0 1 6 6V16" fill="none" stroke="#2E3440" stroke-width="1.3" stroke-linecap="round"/></svg>
      <svg style="left:291px" width="18" height="17" viewBox="0 0 18 17"><path d="M12 1l4.5 4.5L12 10M16 5.5H8a6 6 0 0 0-6 6V16" fill="none" stroke="#9AA0A8" stroke-width="1.3" stroke-linecap="round"/></svg>
    </div>
    <div class="drawing-area" role="img" aria-label="Drawing canvas with the word Hello handwritten in blue"></div>
    <nav class="tabs">
      <div class="tab"><svg width="16" height="16" viewBox="0 0 16 16"><g fill="none" stroke="#9AA0A8" stroke-width="1.2"><rect x="1" y="1" width="5.5" height="5.5" rx="1.5"/><rect x="9.5" y="1" width="5.5" height="5.5" rx="1.5"/><rect x="1" y="9.5" width="5.5" height="5.5" rx="1.5"/><rect x="9.5" y="9.5" width="5.5" height="5.5" rx="1.5"/></g></svg>Show all word</div>
      <div class="tab active"><svg width="16" height="16" viewBox="0 0 16 16"><g fill="none" stroke="#0054AA" stroke-width="1.4"><rect x="1" y="1" width="5.5" height="5.5" rx="1.5"/><rect x="9.5" y="1" width="5.5" height="8" rx="1.5"/><rect x="1" y="9.5" width="5.5" height="5.5" rx="1.5"/><rect x="9.5" y="11.5" width="5.5" height="3.5" rx="1.5"/></g></svg>Play all words</div>
    </nav>
    <div class="word-tile" style="left:11px;top:518px;width:146px;height:146px;font-size:24px">Hello,</div>
    <div class="word-tile" style="left:164px;top:518px;width:70px;height:69px;font-size:12px;border-radius:35px">Hope</div>
    <div class="word-tile" style="left:240px;top:518px;width:70px;height:69px;font-size:12px;border-radius:35px">You</div>
    <div class="word-tile" style="left:164px;top:593px;width:146px;height:71px;font-size:18px;border-radius:35px">Are</div>
    <div class="word-tile" style="left:11px;top:671px;width:146px;height:70px;font-size:18px;border-radius:35px">Doing</div>
    <div class="word-tile" style="left:164px;top:671px;width:146px;height:146px;font-size:24px">Fine.</div>
    <div class="primary-button">Show me the results</div>
  </section>

  <!-- NestStats screen -->
  <section class="phone" style="left:802px;top:51px;height:794px">
    <div class="status-bar"><span class="time">9:41</span>
      <svg style="left:261px" width="16" height="12" viewBox="0 0 16 12"><path d="M1 4a10 10 0 0 1 14 0M3.5 6.5a6.5 6.5 0 0 1 9 0M6 9a3 3 0 0 1 4 0" fill="none" stroke="#fff" stroke-width="1.4" stroke-linecap="round"/></svg>
      <svg style="left:285px" width="17" height="11" viewBox="0 0 17 11"><rect x="1" y="1" width="13" height="9" rx="2.5" fill="none" stroke="#fff" stroke-width="1.2"/><rect x="3.5" y="3.5" width="2" height="4" fill="#fff"/><rect x="6.5" y="3.5" width="2" height="4" fill="#fff"/><rect x="15" y="4" width="1.5" height="3" fill="#fff"/></svg>
    </div>
    <header class="app-header">
      <span class="title center">NestStats</span>
      <svg style="left:293px;top:14px" width="16" height="13" viewBox="0 0 16 13"><path d="M1 1h14M1 6.5h10M1 12h7" stroke="#2E3440" stroke-width="1.4" stroke-linecap="round"/></svg>
    </header>
    <div class="avatar" role="img" aria-label="Learner profile photo"></div>

    <div class="pill active" style="left:12px;width:86px">Ranking</div>
    <div class="pill" style="left:108px;width:108px">Correct word</div>
    <div class="pill" style="left:223px;width:110px;border-radius:20px 0 0 20px">Todo list...</div>

    <div class="rank-card" style="left:12px;width:222px">
      <div class="badge" style="left:15px;top:20px">
        <svg width="22" height="22" viewBox="0 0 22 22"><path d="M6 3h10v5a5 5 0 0 1-10 0zM6 5H3v1.5A3.5 3.5 0 0 0 6.5 10M16 5h3v1.5A3.5 3.5 0 0 1 15.5 10M11 13v4M7 19h8" fill="none" stroke="#00A9DD" stroke-width="1.5" stroke-linecap="round"/></svg>
      </div>
      <span class="label">Total ranking</span>
      <span class="value">1<small>of</small>100</span>
    </div>
    <div class="rank-card" style="left:242px;width:90px;border-radius:43px 0 0 43px">
      <div class="badge" style="left:15px;top:20px">
        <svg width="22" height="22" viewBox="0 0 22 22"><circle cx="11" cy="14" r="5.5" fill="none" stroke="#00A9DD" stroke-width="1.5"/><circle cx="11" cy="14" r="2.2" fill="none" stroke="#00A9DD" stroke-width="1.3"/><path d="M7 2l3 6.5M15 2l-3 6.5" stroke="#00A9DD" stroke-width="1.5" stroke-linecap="round"/></svg>
      </div>
    </div>

    <div class="stat-card" style="top:242px;height:305px">
      <span class="month" style="top:26px">November 2024</span>
      <span class="heading" style="top:45px">Learning curve</span>
      <svg class="chart" width="297" height="305" viewBox="0 0 297 305">
        <text x="283" y="70" text-anchor="end">word per day</text>
        <g stroke="#ECEEF0" stroke-width="1">
          <line x1="15" y1="86" x2="260" y2="86"/><line x1="15" y1="122" x2="260" y2="122"/>
          <line x1="15" y1="158" x2="260" y2="158"/><line x1="15" y1="194" x2="260" y2="194"/>
          <line x1="15" y1="230" x2="260" y2="230"/><line x1="15" y1="266" x2="260" y2="266"/>
        </g>
        <g>
          <text x="262" y="90">100</text><text x="262" y="126">50</text><text x="262" y="162">30</text>
          <text x="262" y="198">20</text><text x="262" y="234">10</text><text x="262" y="270">0</text>
          <text x="27" y="283" text-anchor="middle">23</text><text x="61" y="283" text-anchor="middle">24</text>
          <text x="95" y="283" text-anchor="middle">25</text><text x="128" y="283" text-anchor="middle">26</text>
          <text x="162" y="283" text-anchor="middle">27</text><text x="196" y="283" text-anchor="middle">28</text>
          <text x="230" y="283" text-anchor="middle">29</text>
        </g>
        <path d="M26 258C45 258 60 255 70 252S85 260 97 258S120 243 130 242S147 226 160 228S183 242 195 236S225 208 232 165" fill="none" stroke="#0054AA" stroke-width="1.5" stroke-linecap="round"/>
        <circle cx="232" cy="165" r="6" fill="#C7EBF8" opacity=".7"/>
        <circle cx="232" cy="165" r="2.3" fill="#0054AA"/>
      </svg>
    </div>

    <div class="stat-card" style="top:564px;height:208px">
      <span class="month" style="top:26px">November 2024</span>
      <span class="heading" style="top:45px">Recently learned word</span>
      <div class="word-row" style="top:69px;font-weight:400">EI</div>
      <div class="word-row" style="top:105px">ELA</div>
      <div class="word-row" style="top:141px">Lorem</div>
      <div class="word-row" style="top:177px;height:1px;padding:0"></div>
    </div>
  </section>

</main>
</body>
</html>
```